Northfield Builders Guild Business card

We are looking for a new business card design with photo included.
Our business is a nonprofit construction contractor membership organization. We offer business education, assist with business setup and licensing, provide safety training, and provide a member directory.
URL: www.brickwayguildnetwork.org
Color code:
CMYK: 0 cyan, 42 magenta, 100 yellow, 0 black for Print.
Hexidecimal: #FF9900
RGB: R 255; G 153; B 0

```html
<!DOCTYPE html>
<html lang="en">
<head>
<meta charset="utf-8">
<title>Northfield Builders Guild – Business Card</title>
<link href="https://fonts.googleapis.com/css2?family=Open+Sans:wght@400;600;800&display=swap" rel="stylesheet">
<style>
  :root {
    --stage: #2a2a2a;
    --card: #1c1c1c;
    --orange: #ff9900;
    --white: #ffffff;
    --grey: #6f6f6f;
  }
  * { margin: 0; padding: 0; box-sizing: border-box; }
  html, body {
    width: 1200px; height: 900px; overflow: hidden;
    background: var(--stage);
    font-family: "Open Sans", Arial, sans-serif;
  }
  .canvas {
    width: 1200px; height: 900px;
    display: flex; flex-direction: column;
    align-items: center; justify-content: center; gap: 40px;
  }
  .card {
    position: relative;
    width: 640px; height: 366px;
    background: var(--card);
    border-bottom: 7px solid var(--orange);
    box-shadow: 0 10px 30px rgba(0,0,0,.45);
  }
  /* front */
  .card-front { display: flex; align-items: center; padding: 0 44px; }
  .brand {
    width: 250px;
    color: var(--white);
    font-weight: 800;
    font-size: 30px;
    line-height: 1.05;
    text-transform: uppercase;
    letter-spacing: .5px;
  }
  .divider {
    width: 2px; height: 170px;
    background: var(--orange);
    margin: 0 30px;
  }
  .contact { color: var(--white); font-size: 15px; line-height: 1.5; }
  .contact-name {
    color: var(--orange); font-weight: 600; font-size: 20px;
    text-transform: uppercase; line-height: 1.2;
  }
  .contact-role { margin-bottom: 6px; }
  .contact-address { margin-bottom: 6px; }
  .contact-line { display: flex; align-items: center; gap: 8px; }
  .contact-line svg { width: 13px; height: 13px; flex: none; }
  /* back */
  .card-back { display: flex; align-items: center; justify-content: center; }
  .brand-back {
    color: var(--grey);
    font-weight: 800;
    font-size: 46px;
    line-height: 1.05;
    text-transform: uppercase;
    text-align: center;
  }
</style>
</head>
<body>
<main class="canvas">
  <section class="card card-front">
    <div class="brand">Northfield Builders Guild</div>
    <div class="divider"></div>
    <div class="contact">
      <div class="contact-name">Dana Holloway</div>
      <div class="contact-role">President</div>
      <div class="contact-address">2400 NW Alder Ridge Rd., Suite #210<br>Salem, OR 97301</div>
      <div class="contact-line">
        <svg viewBox="0 0 16 16" aria-hidden="true"><path fill="var(--orange)" d="M3.5 1l2.5 3-1.5 2c1 2 2.5 3.5 4.5 4.5l2-1.5 3 2.5-1.5 2.5C7 14 2 9 1 3z"/></svg>
        <span>(503) 555-0148</span>
      </div>
      <div class="contact-line">
        <svg viewBox="0 0 16 16" aria-hidden="true"><rect x="1" y="3" width="14" height="10" fill="var(--orange)"/><path d="M1 3l7 6 7-6" fill="none" stroke="var(--card)" stroke-width="1.5"/></svg>
        <span>support@nbguild.org</span>
      </div>
      <div class="contact-line">
        <svg viewBox="0 0 16 16" aria-hidden="true"><circle cx="8" cy="8" r="6.5" fill="none" stroke="var(--orange)" stroke-width="1.6"/><path d="M1.5 8h13M8 1.5c-3 3.5-3 9.5 0 13M8 1.5c3 3.5 3 9.5 0 13" fill="none" stroke="var(--orange)" stroke-width="1.2"/></svg>
        <span>www.brickwayguildnetwork.org</span>
      </div>
    </div>
  </section>

  <section class="card card-back">
    <div class="brand-back">Northfield<br>Builders Guild</div>
  </section>
</main>
</body>
</html>
```